We need business cards for our Kashmiri Indian Takeaway Shop. our business sells authentic Kashmiri Cuisine. We also offer catering services and have a BYO Function Room available for private bookings. We would like to see simple but stylish designs that feature Moroccan or Arabic style patterns/ borders and use golds, deep reds, pearl/cream and a touch of black or white. We do not want pictures of curries or Indian spices, chillies etc. The final design should communicate sumptuous, exotic dining.

Target Market(s)

Indian food lovers

Industry/Entity Type

Catering

Contact Information for Business Card

Rafi's Kitchen Authentic Kashmiri Indian Cuisine

Colors
ec2027
fce8d3
fcca95
faa54b

Requirements
Must have
• Simple but stylish design, using Moroccan/Arabic inspired borders or features
Should not have
• Pictures of curries, spices, food etc

```html
<!DOCTYPE html>
<html lang="en">
<head>
<meta charset="utf-8">
<title>Rafi's Kitchen – Business Card</title>
<link href="https://fonts.googleapis.com/css2?family=Open+Sans:wght@400;600&display=swap" rel="stylesheet">
<style>
  :root {
    --page-bg: #e9e4dc;
    --card-edge: #050404;
    --card-dark: #140d0a;
    --card-glow: #4a3026;
    --band-tone: #3b3223;
    --band-hole: #0d0b09;
    --gold: #d7ac42;
    --gold-light: #f1cf6d;
    --gold-deep: #8f6a1c;
  }
  * { margin: 0; padding: 0; box-sizing: border-box; }
  html, body {
    width: 1200px; height: 900px; overflow: hidden;
    background: var(--page-bg);
  }
  .canvas {
    position: relative; width: 1200px; height: 900px;
  }
  .business-card {
    position: absolute; left: 100px; top: 164px;
    width: 1000px; height: 572px;
    overflow: hidden;
    background: radial-gradient(ellipse 55% 60% at 62% 40%, var(--card-glow) 0%, #2a1a14 45%, var(--card-dark) 100%);
    box-shadow: 0 18px 40px rgba(0,0,0,0.35);
    font-family: "Open Sans", Verdana, sans-serif;
  }
  .edge-strip {
    position: absolute; left: 0; top: 0; width: 52px; height: 100%;
    background: var(--card-edge);
  }
  .pattern-band {
    position: absolute; left: 52px; top: 0; width: 235px; height: 100%;
    background: var(--band-tone);
  }
  .band-holes {
    position: absolute; left: 52px; top: 0; width: 300px; height: 100%;
  }
  .emblem-ornament {
    position: absolute; left: 95px; top: 70px; width: 230px; height: 400px;
    border-radius: 45% 55% 50% 50%;
    background: radial-gradient(ellipse at 45% 45%, var(--gold-light) 0%, var(--gold) 45%, rgba(143,106,28,0.55) 75%, rgba(143,106,28,0) 100%);
  }
  .card-text {
    position: absolute; left: 0; top: 0; width: 100%; height: 100%;
    color: var(--gold);
    text-shadow: 0 2px 2px rgba(0,0,0,0.6);
  }
  .brand-name, .tagline {
    position: absolute; left: 360px; width: 560px; text-align: center;
  }
  .brand-name { top: 50px; font-size: 30px; }
  .tagline { top: 92px; font-size: 31px; }
  .owner-line {
    position: absolute; left: 400px; top: 185px;
    font-size: 33px; font-weight: 600;
  }
  .contact-list {
    position: absolute; left: 395px; top: 298px;
    list-style: none; font-size: 23px; line-height: 31px;
  }
</style>
</head>
<body>
<div class="canvas">
  <div class="business-card">
    <div class="edge-strip"></div>
    <div class="pattern-band" role="img" aria-label="Gold speckled textured band"></div>
    <svg class="band-holes" width="300" height="572" viewBox="0 0 300 572">
      <circle cx="120" cy="120" r="16" fill="var(--band-hole)"/>
      <circle cx="165" cy="175" r="14" fill="var(--band-hole)"/>
      <circle cx="238" cy="205" r="15" fill="var(--band-hole)"/>
      <circle cx="95" cy="330" r="15" fill="var(--band-hole)"/>
      <circle cx="150" cy="390" r="16" fill="var(--band-hole)"/>
      <circle cx="250" cy="300" r="14" fill="var(--band-hole)"/>
    </svg>
    <div class="emblem-ornament" role="img" aria-label="Gold Arabic-style calligraphic ornament"></div>
    <div class="card-text">
      <p class="brand-name">Rafi's Kitchen</p>
      <p class="tagline">Authentic Kashmiri Indian Cuisine</p>
      <p class="owner-line">Rafi Mirza, Owner &amp; Chef</p>
      <ul class="contact-list">
        <li>Takeaway Shop &amp; Catering</li>
        <li>BYO Function Room - bookings essential</li>
        <li>14B Marlin Street, Yungaburra Qld</li>
        <li>07- 4055 1837</li>
      </ul>
    </div>
  </div>
</div>
</body>
</html>
```